Consultancy company needs flyer design

We need a flyer design for a new service to be provided. It is a service in which project management is outsourced. Text of the service has been attached (in Dutch).
We would like the design to be in line with our website design (www.velostrin.com). Also we would like to re-use the main banner of the site (see attachment)

Industry/Entity Type

It Company

Requirements
Must have
• Flyer must be double sided

```html
<!DOCTYPE html>
<html lang="nl">
<head>
<meta charset="utf-8">
<title>Velostrin – PMAAS flyer</title>
<link href="https://fonts.googleapis.com/css2?family=Open+Sans:wght@300;400;600;700;800&display=swap" rel="stylesheet">
<style>
:root{
  --brown:#7d6a45;
  --brown-dark:#5f5035;
  --grey-band:#e6e7e6;
  --slate:#595959;
  --ink:#3a3a3a;
  --ink-soft:#555;
  --paper:#ffffff;
  --stage:#2b2b2b;
}
*{box-sizing:border-box;margin:0;padding:0}
html,body{width:1200px;height:960px;overflow:hidden;background:var(--stage);font-family:"Open Sans",Arial,sans-serif;color:var(--ink)}
.page{position:absolute;top:119px;width:524px;height:740px;background:var(--paper);overflow:hidden}
.page--front{left:58px}
.page--back{left:627px}
.abs{position:absolute}

/* front */
.brand{left:0;right:0;top:34px;display:flex;justify-content:center}
.brand__text{font-weight:700;font-size:28px;line-height:1;color:var(--ink)}
.brand__text small{display:block;font-size:10px;letter-spacing:1px;margin-top:4px}
.hero-band{left:0;right:0;top:105px;height:73px;background:var(--brown);color:#fff;text-align:center;padding-top:10px}
.hero-band h1{font-size:21px;font-weight:800;line-height:1.2;letter-spacing:.2px}
.hero-band p{font-size:23px;font-weight:300;line-height:1.2}
.intro{left:26px;right:24px;top:190px;font-size:10.6px;line-height:1.38;color:var(--ink)}
.pain{left:0;right:0;top:245px;height:89px;background:var(--grey-band);display:flex;padding:8px 0 0 26px}
.pain ul{list-style:none;width:240px;font-size:8.6px;line-height:1.38;color:var(--ink-soft)}
.pain ul+ul{border-left:1px solid #a9a9a9;padding-left:24px;height:75px;width:234px}
.pain li{position:relative;padding-left:12px;margin-bottom:7px}
.pain li::before{content:"";position:absolute;left:0;top:4px;width:5px;height:5px;border-radius:50%;background:var(--brown)}
.banner{left:0;right:0;top:346px;height:351px;background:linear-gradient(135deg,#1d2a3a 0%,#6f8ea8 35%,#b9d1de 55%,#4c6e8a 75%,#15202c 100%)}
.banner__caption{left:0;right:0;top:263px;height:76px;background:rgba(30,30,34,.78);color:#fff;text-align:center;padding-top:10px}
.banner__caption h2{font-size:30px;font-weight:700;line-height:1.1;letter-spacing:.5px}
.banner__caption p{font-size:13px;font-weight:400;margin-top:7px}
.front-foot{left:0;right:0;top:704px;height:36px;background:var(--brown);display:flex;align-items:center;color:#fff;font-size:11.5px;white-space:nowrap}
.front-foot__label{position:relative;flex:none;height:36px;width:106px;background:var(--slate);display:flex;align-items:center;padding-left:19px;font-size:13px}
.front-foot__label svg{position:absolute;right:-10px;top:0}
.front-foot .contact{display:flex;align-items:center;gap:7px;padding:0 11px;border-right:1px solid rgba(255,255,255,.5);height:18px}
.front-foot .contact:first-of-type{padding-left:20px}
.front-foot .contact:last-child{border:0}

/* back */
.lead{left:0;right:0;top:22px;height:109px;background:var(--grey-band);padding:14px 23px 0;font-size:10.6px;line-height:1.38;text-align:justify;color:var(--ink-soft)}
.tab{height:29px;background:var(--brown);color:#fff;font-size:13.5px;font-weight:600;display:flex;align-items:center;padding-left:18px}
.tab--slate{background:var(--slate);font-weight:400}
.checks{list-style:none;font-size:8.6px;line-height:1.38;color:var(--ink-soft)}
.checks li{position:relative;padding-left:20px;margin-bottom:7px}
.checks li::before{content:"";position:absolute;left:0;top:3px;width:7px;height:7px;border:1.3px solid var(--brown-dark)}
.summary{left:282px;top:379px;font-size:15px;line-height:1.35;color:var(--ink)}
.summary b{color:var(--brown);font-weight:600}
.body-col{font-size:8.3px;line-height:1.45;text-align:justify;color:var(--ink-soft)}
.back-foot{left:0;right:0;top:654px;height:86px;background:var(--brown);color:#fff}
.back-foot h3{text-align:center;font-size:24px;font-weight:400;margin-top:7px}
.back-foot .row{display:flex;justify-content:center;margin-top:6px;font-size:14px;white-space:nowrap}
.back-foot .contact{display:flex;align-items:center;gap:12px;padding:4px 15px;border-right:1px solid rgba(255,255,255,.6)}
.back-foot .contact:last-child{border:0}
</style>
</head>
<body>

<section class="page page--front">
  <div class="abs brand">
    <div class="brand__text">velostrin<small>BUSINESS IMPROVEMENT</small></div>
  </div>

  <header class="abs hero-band">
    <h1>ONTZORGING VAN UW PROJECTDELIVERY:</h1>
    <p>Project Management As a Service (PMAAS)</p>
  </header>

  <p class="abs intro">U kunt voor de realisatie van uw projectportfolio de hulp inroepen van externe projectmanagers, en daarbij zelf de coördinatie verzorgen. Grote kans dat u dan tegen één of meer van de volgende zaken aan loopt:</p>

  <div class="abs pain">
    <ul>
      <li>Een wisselende kwaliteit van projectmanagers</li>
      <li>Problemen om kosten inzichtelijk en voorspelbaar of beheersbaar houden (management rapportage)</li>
      <li>Een ad hoc relatie met uw projectmanagers en leveranciers</li>
    </ul>
    <ul>
      <li>Beperkt leergedrag en herhaling van fouten</li>
      <li>Tijdverlies en kosten omdat u veel tijd kwijt bent aan uitleg van rand voorwaardelijke zaken</li>
    </ul>
  </div>

  <div class="abs banner" role="img" aria-label="Website banner: close-up of interlocking chrome gears in cool blue light">
    <div class="abs banner__caption">
      <h2>VISUALIZATION</h2>
      <p>EXPERIENTIAL CHANGE BY VISUALIZATION AND SIMULATION</p>
    </div>
  </div>

  <footer class="abs front-foot">
    <div class="front-foot__label">Meer weten
      <svg width="12" height="36" viewBox="0 0 12 36"><path d="M0 0 L11 18 L0 36" fill="var(--slate)" stroke="#fff" stroke-width="1.2"/></svg>
    </div>
    <span class="contact"><svg width="11" height="11" viewBox="0 0 12 12" fill="none" stroke="#fff" stroke-width="1"><circle cx="6" cy="6" r="5"/><ellipse cx="6" cy="6" rx="2.2" ry="5"/><path d="M1 6h10"/></svg>www.velostrin.com</span>
    <span class="contact"><svg width="12" height="10" viewBox="0 0 12 10" fill="#fff"><path d="M0 3 Q6 -1 12 3 L10 4.5 L8.5 3 L3.5 3 L2 4.5Z"/><rect x="2.5" y="5" width="7" height="5" rx="1"/></svg>085 - 0047391</span>
    <span class="contact"><svg width="12" height="9" viewBox="0 0 12 9" fill="none" stroke="#fff" stroke-width="1"><rect x=".5" y=".5" width="11" height="8"/><path d="M.5 .5 6 5l5.5-4.5"/></svg>Info@velostrin.com</span>
  </footer>
</section>

<section class="page page--back">
  <p class="abs lead">Een alternatief is onze PMAAS-service. Die bevat alle ingrediënten om uw projectenportfolio kostenefficiënt en op hoog kwaliteitsniveau te realiseren. Velostrin zorgt voor inzet van projectmanagers die al 'up to speed' zijn als ze bij u binnenkomen. Ze hebben de juiste expertise, zijn al ingewerkt op uw of onze standaard methodiek en op uw organisatorische setting. En heeft u ineens meer of minder werk? Geen probleem. Dan schalen wij net zo gemakkelijk op en af.</p>

  <div class="abs tab" style="top:152px;left:0;width:130px">Wij zorgen voor</div>
  <ul class="abs checks" style="top:196px;left:19px;width:225px">
    <li>een eenduidige werkwijze, rapportering en gebruik van tooling</li>
    <li>een scherpe intake en voorbereidingsfase van de te starten projecten</li>
    <li>de benodigde op-en afschaling van project managers met het juiste profiel</li>
    <li>ingewerkte projectmanagers op de overeengekomen projectmethode</li>
  </ul>
  <ul class="abs checks" style="top:196px;left:282px;width:215px">
    <li>continue monitoring op afgesproken KPI's over de projecten heen</li>
    <li>periodiek overleg over de performance</li>
    <li>continue verbetering op basis van klantevaluaties</li>
    <li>facturatie volgens afspraak (milestone-based)</li>
  </ul>

  <div class="abs tab" style="top:334px;left:0;width:130px">U zorgt voor:</div>
  <ul class="abs checks" style="top:380px;left:19px;width:235px">
    <li style="margin-bottom:13px">een up to date forecast van de te realiseren projectportfolio</li>
    <li>een goede projectbrief als basis voor onze intake</li>
  </ul>

  <p class="abs summary"><b>Kortom:</b> laat u ontzorgen<br>in uw project delivery!</p>

  <div class="abs tab tab--slate" style="top:452px;left:0;width:130px">PMO en PPM</div>
  <div class="abs tab tab--slate" style="top:452px;left:285px;width:117px">PMO en PPM</div>

  <p class="abs body-col" style="top:497px;left:23px;width:205px">Wilt u zich nog meer laten ontzorgen? Dat kan! Naast onze PMAAS-service leveren wij ook diensten op het gebied van Project Management Office (PMO) en/of Project Portfolio Management (PPM). Wij kunnen deze activiteiten voor u opzetten, maar ook de operationele aansturing ervan ondersteunen of voor onze rekening nemen.</p>
  <p class="abs body-col" style="top:497px;left:285px;width:214px">Als management consultancy bureau houden wij ons bezig met de begeleiding van veranderingen in bedrijven. Op het gebied van strategie, maar ook van processen en systemen. Wij onderscheiden ons door toepassing van visualisatie technieken, bedrijfsproces simulaties en unieke services en zijn continu op zoek naar nieuwe toepassingsmogelijkheden op dit gebied. Door de krachten van uw medewerkers en die van ons te verenigen, komen we tot betere en snellere resultaten. Daarbij gaan wij samen op reis. Want veranderingen kun je niet leren, je moet ze ervaren.</p>

  <footer class="abs back-foot">
    <h3>Meer weten</h3>
    <div class="row">
      <span class="contact"><svg width="14" height="14" viewBox="0 0 12 12" fill="none" stroke="#fff" stroke-width=".9"><circle cx="6" cy="6" r="5"/><ellipse cx="6" cy="6" rx="2.2" ry="5"/><path d="M1 6h10"/></svg>www.velostrin.com</span>
      <span class="contact"><svg width="15" height="12" viewBox="0 0 12 10" fill="#fff"><path d="M0 3 Q6 -1 12 3 L10 4.5 L8.5 3 L3.5 3 L2 4.5Z"/><rect x="2.5" y="5" width="7" height="5" rx="1"/></svg>085 - 0047391</span>
      <span class="contact"><svg width="14" height="10" viewBox="0 0 12 9" fill="none" stroke="#fff" stroke-width="1"><rect x=".5" y=".5" width="11" height="8"/><path d="M.5 .5 6 5l5.5-4.5"/></svg>Info@velostrin.com</span>
    </div>
  </footer>
</section>

</body>
</html>
```